Beer can label design for 3 beers!

We are a new brewery called 'Grim Syndicate Brewing' who needs three distinct but cohesive labels for our beer and want a modern, edgy, and imposing design to launch our beers. The concept for our brewery is based on evil movie corporations such as Tarvick Consolidated from Drift and Halvern Market Industries from Gearsmith, so you can draw inspiration from those types of fictional evil corporations. Our brand conveys an evil presence, but is not 'evil' so no devils or anything too dark. The template for the label and guidelines are attached and must be adhered to as they are required to submit a can design in this format. Also included is our font file and logo vector file which cannot be changed apart from separating the hop image from the 'Grim Syndicate Brewing' text. We would like to use a black background for the can design. Some of the details for the beer may change, so please use the text specified below (or placeholder text if no detail is given below so that we can update the text later) and proposed font. If your design is chosen, we would require two versions of each label - one for a 473 ml can and one scaled up for a 355 ml can. Please read through all the requirements provided in the documentation provided.
First Label (use the 473 ml can template)
Beer Name: MBX (Merger Bridge Exchange) IPA
Beer Style: India Pale Ale
Beer ABV: 6.5%
Barcode: use a generic placeholder
Quantity: 473 ml
Can Design Background: Black
Label must indicate the words "Strong Beer" (must be on the front panel)
Ingredients: malt, hops
Location of Brewery: Calgary, Alberta
Second Label (use the 473 ml can template)
Beer Name: Ledger Audit Pale Ale
Beer Style: Ale
Beer ABV: 5.5 % alc./vol (must be on front panel)
Quantity: 473 ml
Can Design Background: Red or White?
Ingredients: malt, hops
Third Label (use the 473 ml can template)
Beer Name: Margin Call Porter
Beer Style: Porter
Beer ABV: 5.5%
Quantity: 473 ml
Ingredients: malt, hops
Craft Brewery

```html
<!DOCTYPE html>
<html lang="en">
<head>
<meta charset="utf-8">
<title>Grim Syndicate Brewing – Can Labels</title>
<link rel="stylesheet" href="https://fonts.googleapis.com/css2?family=Russo+One&family=Exo+2:wght@500;600;700&display=swap">
<style>
  :root {
    --page-bg: #eceef0;
    --red: #d8343b;
    --red-light: #e8535a;
    --red-deep: #8e2a2f;
    --frame-line: #8a8a8a;
    --white-body: #f7f7f7;
    --maroon-body: #4b1d1f;
    --black-body: #1b1b1c;
    --ink-dark: #1d1d1d;
    --ink-light: #ffffff;
  }
  * { box-sizing: border-box; margin: 0; padding: 0; }
  html, body { width: 1200px; height: 990px; overflow: hidden; }
  body {
    background: radial-gradient(ellipse at 50% 40%, #f8f9fa 0%, var(--page-bg) 70%);
    font-family: "Exo 2", sans-serif;
    position: relative;
  }
  .can {
    position: absolute;
    top: 100px;
    width: 270px;
    height: 720px;
    background: var(--body);
    color: var(--ink);
    overflow: hidden;
    box-shadow: 0 6px 24px rgba(0,0,0,.12);
  }
  .can--porter { left: 105px; --body: var(--white-body); --ink: var(--ink-dark); --mark: var(--ink-dark); }
  .can--ledger { left: 465px; --body: var(--maroon-body); --ink: var(--ink-light); --mark: var(--ink-light); }
  .can--mbx    { left: 825px; --body: var(--black-body); --ink: var(--ink-light); --mark: var(--ink-light); }

  .can__top-band {
    position: absolute; left: 0; top: 0; width: 100%; height: 38px;
    background: linear-gradient(180deg, var(--red-light), var(--red));
  }
  .brand { position: absolute; top: 62px; left: 0; width: 100%; text-align: center; }
  .brand__dot {
    width: 58px; height: 58px; border-radius: 50%;
    background: var(--mark); margin: 0 auto 16px;
  }
  .brand__name {
    font-family: "Exo 2", sans-serif; font-weight: 600;
    font-size: 17px; letter-spacing: 1px; text-transform: uppercase;
    color: var(--ink);
  }
  .brand__sub {
    display: flex; align-items: center; justify-content: center; gap: 6px;
    font-weight: 700; font-size: 10px; letter-spacing: 2px; color: var(--red);
    text-transform: uppercase; margin-top: 1px;
  }
  .brand__sub::before, .brand__sub::after {
    content: ""; width: 58px; height: 1.5px; background: var(--red);
  }
  .can__frame { position: absolute; left: 0; top: 205px; width: 270px; height: 380px; }
  .title {
    position: absolute; left: 0; width: 100%; text-align: center;
    font-family: "Russo One", sans-serif; text-transform: uppercase; color: var(--ink);
    line-height: 1;
  }
  .title--porter { top: 352px; font-size: 50px; letter-spacing: -1px; }
  .title--ledger { top: 320px; font-size: 50px; line-height: 1.1; }
  .title--mbx { top: 318px; font-size: 80px; letter-spacing: 1px; }
  .tagline {
    position: absolute; left: 0; width: 100%; text-align: center;
    font-family: "Russo One", sans-serif; font-size: 12px; color: var(--red);
    text-transform: uppercase; letter-spacing: .5px;
  }
  .can--porter .tagline { top: 460px; }
  .can--mbx .tagline { top: 412px; font-size: 11px; }
  .specs {
    position: absolute; top: 553px; left: 20px; right: 18px;
    display: flex; justify-content: space-between; align-items: flex-end;
    color: var(--ink);
  }
  .specs__volume { font-weight: 600; font-size: 13px; letter-spacing: .5px; }
  .specs__detail { text-align: left; }
  .specs__class { font-size: 9px; font-weight: 500; }
  .specs__abv { font-size: 14px; font-weight: 600; letter-spacing: .3px; }
  .can__base {
    position: absolute; left: 0; bottom: 0; width: 100%; height: 112px;
    background: linear-gradient(180deg, var(--red) 0%, var(--red-light) 55%, var(--red) 100%);
  }
  .style-tab {
    position: absolute; top: 597px; left: 17px; width: 236px; height: 50px;
    background: var(--red-deep);
    clip-path: polygon(6% 0, 94% 0, 100% 100%, 0 100%);
    display: flex; align-items: center; justify-content: center;
    font-family: "Russo One", sans-serif; font-size: 20px; color: var(--ink-light);
    text-transform: uppercase; white-space: nowrap;
  }
</style>
</head>
<body>

  <section class="can can--porter">
    <div class="can__top-band"></div>
    <div class="brand">
      <div class="brand__dot"></div>
      <div class="brand__name">Grim Syndicate</div>
      <div class="brand__sub">Brewing</div>
    </div>
    <svg class="can__frame" viewBox="0 0 270 380" aria-hidden="true">
      <path d="M75 12 H195 L250 75 V280 L195 340 H75 L20 280 V75 Z" fill="none" stroke="var(--frame-line)" stroke-width="1.3" stroke-linejoin="round"/>
      <path d="M12 90 C8 300 40 356 135 356 C230 356 262 300 258 90 C270 320 230 378 135 378 C40 378 0 320 12 90 Z" fill="var(--red)"/>
    </svg>
    <h2 class="title title--porter">Porter</h2>
    <p class="tagline">Strong Beer</p>
    <div class="specs">
      <span class="specs__volume">473 ML</span>
      <div class="specs__detail">
        <div class="specs__class">Strong Beer / Bière Forte</div>
        <div class="specs__abv">5.5% ALC./VOL.</div>
      </div>
    </div>
    <div class="can__base"></div>
    <div class="style-tab">Porter</div>
  </section>

  <section class="can can--ledger">
    <div class="can__top-band"></div>
    <div class="brand">
      <div class="brand__dot"></div>
      <div class="brand__name">Grim Syndicate</div>
      <div class="brand__sub">Brewing</div>
    </div>
    <svg class="can__frame" viewBox="0 0 270 380" aria-hidden="true">
      <path d="M75 12 H195 L250 75 V280 L195 340 H75 L20 280 V75 Z" fill="none" stroke="var(--frame-line)" stroke-width="1.3" stroke-linejoin="round"/>
      <path d="M12 90 C8 300 40 356 135 356 C230 356 262 300 258 90 C270 320 230 378 135 378 C40 378 0 320 12 90 Z" fill="var(--red)"/>
    </svg>
    <h2 class="title title--ledger">Ledger<br>Audit</h2>
    <div class="specs">
      <span class="specs__volume">473 ML</span>
      <div class="specs__detail">
        <div class="specs__class">Strong Beer / Bière Forte</div>
        <div class="specs__abv">5.5% ALC./VOL.</div>
      </div>
    </div>
    <div class="can__base"></div>
    <div class="style-tab">Pale Ale</div>
  </section>

  <section class="can can--mbx">
    <div class="can__top-band"></div>
    <div class="brand">
      <div class="brand__dot"></div>
      <div class="brand__name">Grim Syndicate</div>
      <div class="brand__sub">Brewing</div>
    </div>
    <svg class="can__frame" viewBox="0 0 270 380" aria-hidden="true">
      <path d="M75 12 H195 L250 75 V280 L195 340 H75 L20 280 V75 Z" fill="none" stroke="var(--frame-line)" stroke-width="1.3" stroke-linejoin="round"/>
      <path d="M12 90 C8 300 40 356 135 356 C230 356 262 300 258 90 C270 320 230 378 135 378 C40 378 0 320 12 90 Z" fill="var(--red)"/>
    </svg>
    <h2 class="title title--mbx">MBX</h2>
    <p class="tagline">Merger Bridge Exchange</p>
    <div class="specs">
      <span class="specs__volume">473 ML</span>
      <div class="specs__detail">
        <div class="specs__class">Strong Beer / Bière Forte</div>
        <div class="specs__abv">6.5% ALC./VOL.</div>
      </div>
    </div>
    <div class="can__base"></div>
    <div class="style-tab">India Pale Ale</div>
  </section>

</body>
</html>
```